Sales PowerPoint Template to help us attract new customers

We need to create a generic PowerPoint template for our organization. We are in the commercial facilities industry, servicing convenience, restaurants, grocery, and retail customers in the US. We handle trades such as HVAC, Refrigeration, Plumbing, Electrical, Food Equipment, Coffee, etc.

We need to incorporate our new logo, updated colors, Font (Arial). We want it to stand out in this deck and avoid looking like all other facility companies. We want to make sure the template size is not too large (less than 20 MB), so it prevent people to edit/send.
Attached are new logo, colors, old powerpoint template, and finally the "New Design to Incorporate into Template" is new materials we're looking to leverage. This might give you ideas.

Create at least 10 slides (1 cover, 1 agenda slide, at least 7 general slides, and 1 wrap-up slide)

Target Market(s)

Convenience Stores, Retail Stores, Groceries, and Restaurants in the US

Industry/Entity Type

Facilities Services (HVAC, Refrigeration, Plumbing, Electrical, etc, repair and preventative maintenance)

Font styles to use
Other font styles liked:
• Arial

Requirements
Must have
• Follow company colors and font (Arial)
Should not have
• Not approved company colors, font

```html
<!DOCTYPE html>
<html lang="en">
<head>
<meta charset="UTF-8">
<title>Thank You</title>
<link href="https://fonts.googleapis.com/css2?family=Montserrat:wght@300;800&family=Arimo:wght@400&display=swap" rel="stylesheet">
<style>
  :root {
    --olive: #87952b;
    --accent: #f5a100;
    --body-grey: #595959;
    --ink: #1a1a1a;
    --band: #f3f3ec;
    --paper: #ffffff;
  }
  html, body {
    margin: 0;
    padding: 0;
    overflow: hidden;
    background: var(--paper);
  }
  .slide {
    position: relative;
    width: 1200px;
    height: 676px;
    overflow: hidden;
    background: var(--paper);
  }
  .backdrop-band {
    position: absolute;
    left: 634px;
    top: 302px;
    width: 566px;
    height: 94px;
    background: var(--band);
    border-top-left-radius: 56px;
  }
  .headline {
    position: absolute;
    left: 0;
    top: 170px;
    width: 1200px;
    margin: 0;
    text-align: center;
    font-family: "Montserrat", sans-serif;
    font-weight: 800;
    font-size: 91px;
    letter-spacing: -3px;
    line-height: 1;
    color: var(--olive);
  }
  .intro {
    position: absolute;
    left: 340px;
    top: 325px;
    width: 560px;
    margin: 0;
    text-align: center;
    font-family: Arial, "Arimo", sans-serif;
    font-size: 17.5px;
    line-height: 26px;
    color: var(--body-grey);
  }
  .contact {
    position: absolute;
    display: flex;
    align-items: flex-start;
    gap: 14px;
    font-family: "Montserrat", sans-serif;
    font-weight: 300;
    font-size: 23.5px;
    line-height: 28px;
    color: var(--ink);
  }
  .contact svg {
    flex: none;
    width: 24px;
    height: 24px;
    margin-top: 2px;
    fill: var(--accent);
  }
  .contact-phone   { left: 353px; top: 464px; }
  .contact-address { left: 353px; top: 505px; }
  .contact-email   { left: 628px; top: 463px; gap: 12px; }
  .contact-web     { left: 628px; top: 506px; gap: 12px; }
</style>
</head>
<body>
  <main class="slide">
    <div class="backdrop-band" aria-hidden="true"></div>

    <h1 class="headline">THANK YOU!</h1>

    <p class="intro">
      Lorem ipsum dolor sit amet, consectetur adipiscing elit, sed do<br>
      eiusmod tempor incididunt ut labore et dolore magna aliqua.<br>
      Quis ipsum suspendisse ultrices gravida.
    </p>

    <div class="contact contact-phone">
      <svg viewBox="0 0 24 24" aria-hidden="true"><path d="M6.6 10.8a15.1 15.1 0 0 0 6.6 6.6l2.2-2.2c.3-.3.7-.4 1-.2 1.1.4 2.3.6 3.6.6.6 0 1 .4 1 1V20c0 .6-.4 1-1 1A17 17 0 0 1 3 4c0-.6.4-1 1-1h3.5c.6 0 1 .4 1 1 0 1.3.2 2.5.6 3.6.1.3 0 .7-.2 1z"/></svg>
      <span>(+1) 123 456 789</span>
    </div>

    <div class="contact contact-address">
      <svg viewBox="0 0 24 24" aria-hidden="true"><path d="M12 2a7 7 0 0 0-7 7c0 5.2 7 13 7 13s7-7.8 7-13a7 7 0 0 0-7-7zm0 9.5A2.5 2.5 0 1 1 12 6.5a2.5 2.5 0 0 1 0 5z"/></svg>
      <span>Lorem ipsum dolor<br>sit amet, City, USA.</span>
    </div>

    <div class="contact contact-email">
      <svg viewBox="0 0 24 24" aria-hidden="true"><path d="M2 5h20v2.2l-10 6.3L2 7.2z"/><path d="M2 9.6l10 6.3 10-6.3V19H2z"/></svg>
      <span>info@trevana.com</span>
    </div>

    <div class="contact contact-web">
      <svg viewBox="0 0 24 24" aria-hidden="true"><path d="M6 2l12 11.5h-6.2l3.4 7.3-2.6 1.2-3.4-7.4L6 18.8z"/></svg>
      <span>www.Trevana.com</span>
    </div>
  </main>
</body>
</html>
```